Pull Up Banner - Recruitment Company

We would like a design for a pull up banner.

For context: we are a recruitment business. We specialise in helping people in healthcare industry to find jobs in Australia.

I have come up with several ideas and text for the banner. Feel free to use the following as you see appropriate:

- Our logo (see attached)
- 'Healthcare Recruitment Agency'
- Some sort of imagine / cartoon of medical professionals (ie. doctor, nurse, physiotherapist, speech pathologist). A cartoon is more friendly than committing to a photo
- 'Empowering your next career move'
- 'Discover tailored opportunities based on your career preferences'
- Dot points (allied health, nursing, medical imaging)
- Contact info at the bottom including our website (www.quellstaffing.com.au, our Instagram handle @quellstaffing, Mobile: XXXX XXX XXX. The title section for contact information could be 'Get in touch:'

Feel free to submit a couple of designs and we can merge aspects that look good on your designs and find the perfect fit.
Thank you
Updates

Hello,

Thank you for your initial submissions to this project. I appreciate the time you've invested.

After reviewing the first attempt, I'd like to share some feedback and initial observations:

- Professionalism and engagement: Is the overall appearance of the banner professional? It's crucial that we have a high-quality design as this will represent our business.

- Image selection: The image (whether cartoon or real people) appears quite generic. Please consider submitting the banner with a few different photos in the middle for us to choose from. Ensure the image is a good fit and not simply a generic stock photo.

- Contact section: Kindly remove the phone number; we no longer wish to include it on the banner. Instead, please include our website (www.quellstaffing.com.au) and Instagram handle (@quellstaffing).

- Color scheme: White, black, and red/pink are preferred, or alternatively, blue. However, please avoid incorporating too many different colors as it may detract from the professional appearance.

We will be printing the design on a banner and require it to look professional and engaging.

Thank you once again for your submissions. I hope the feedback provided above is helpful.

Warm regards,

Target Market(s)

Allied Health Australia

Font styles to use
Serif

Colors
0054AA
0677BA
7BADD7
CADEEF
E8F1F8
0094D4
00A9DD
6FCCEA
C7EBF8
E9F6FB
EB3D1F
EC4F4E
F09395
F8D3D4
FCEDEE

```html
<!DOCTYPE html>
<html lang="en">
<head>
<meta charset="utf-8">
<title>Quell Staffing – Healthcare Recruitment Agency</title>
<link rel="stylesheet" href="https://fonts.googleapis.com/css2?family=Fira+Sans+Extra+Condensed:wght@700&family=League+Spartan:wght@500;600;700&display=swap">
<style>
  :root {
    --ink: #111111;
    --grey: #3f3f40;
    --brand-blue: #0a5fa8;
    --band-blue: #0067b1;
    --sky-pale: #e9f6fb;
    --sky-light: #a9d9f4;
    --sky-mid: #6fc1ec;
    --sky-deep: #22a0e3;
    --white: #ffffff;
  }
  * { box-sizing: border-box; margin: 0; padding: 0; }
  html, body { width: 1200px; height: 2824px; overflow: hidden; background: var(--white); }
  .banner {
    position: relative;
    width: 1200px;
    height: 2824px;
    overflow: hidden;
    background: var(--white);
    font-family: "League Spartan", "Montserrat", sans-serif;
  }
  .hero-sky {
    position: absolute;
    left: 0; top: 0;
    width: 1200px; height: 1620px;
    background: linear-gradient(180deg, var(--white) 0px, var(--white) 300px, #d6ecf9 620px, var(--sky-light) 900px, var(--sky-mid) 1180px, var(--sky-deep) 1480px);
  }
  .doctor-illustration {
    position: absolute;
    z-index: 1;
    left: 700px; top: 345px;
    width: 460px; height: 1150px;
    border-radius: 230px 230px 30px 30px;
    background: linear-gradient(180deg, rgba(255,255,255,0.55), rgba(255,255,255,0.85));
  }
  .brand-name, .headline, .tagline, .intro, .specialties,
  .contact-title, .contact-social, .contact-web { z-index: 3; }
  .brand-name {
    position: absolute;
    left: 86px; top: 96px;
    font-weight: 700;
    font-size: 104px;
    line-height: 1;
    letter-spacing: 2px;
    color: var(--ink);
    text-transform: uppercase;
  }
  .headline {
    position: absolute;
    left: 86px; top: 372px;
    font-family: "Fira Sans Extra Condensed", "Oswald", sans-serif;
    font-weight: 700;
    font-size: 124px;
    line-height: 130px;
    color: var(--brand-blue);
  }
  .tagline {
    position: absolute;
    left: 86px; top: 1196px;
    font-weight: 700;
    font-size: 88px;
    line-height: 72px;
    color: var(--white);
  }
  .wave {
    position: absolute;
    z-index: 2;
    left: 0; top: 1300px;
    width: 1200px; height: 320px;
  }
  .side-stripe {
    position: absolute;
    z-index: 2;
    top: 1530px; bottom: 0;
    background: linear-gradient(180deg, var(--white) 0%, var(--sky-light) 35%, var(--sky-deep) 75%, var(--sky-deep) 100%);
  }
  .side-stripe--thin { left: 85px; width: 16px; }
  .side-stripe--wide { left: 128px; width: 170px; }
  .intro {
    position: absolute;
    left: 370px; top: 1552px;
    width: 810px;
    font-weight: 700;
    font-size: 88px;
    line-height: 93px;
    color: var(--grey);
  }
  .specialties {
    position: absolute;
    left: 372px; top: 1962px;
    list-style: none;
  }
  .specialties li {
    position: relative;
    padding-left: 84px;
    font-weight: 600;
    font-size: 92px;
    line-height: 110px;
    color: var(--brand-blue);
  }
  .specialties li::before {
    content: "";
    position: absolute;
    left: 0; top: 48px;
    width: 20px; height: 20px;
    border-radius: 50%;
    background: var(--brand-blue);
  }
  .contact-title {
    position: absolute;
    left: 370px; top: 2474px;
    font-weight: 700;
    font-size: 66px;
    line-height: 1;
    color: var(--grey);
  }
  .contact-social {
    position: absolute;
    left: 372px; top: 2560px;
    display: flex;
    align-items: center;
    gap: 24px;
  }
  .contact-social .marker {
    width: 70px; height: 70px;
    border: 7px solid var(--grey);
    border-radius: 14px;
  }
  .contact-social span {
    font-weight: 700;
    font-size: 57px;
    color: var(--grey);
  }
  .contact-web {
    position: absolute;
    left: 372px; top: 2642px;
    font-weight: 700;
    font-size: 57px;
    line-height: 1;
    color: var(--grey);
  }
</style>
</head>
<body>
<main class="banner">
  <div class="hero-sky"></div>

  <div class="doctor-illustration" role="img" aria-label="Friendly cartoon doctor in a white coat with a stethoscope, gesturing towards the headline"></div>

  <div class="brand-name">Quell Staffing</div>

  <h1 class="headline">Healthcare<br>Recruitment<br>Agency</h1>

  <p class="tagline">Empowering<br>your next<br>career move</p>

  <svg class="wave" viewBox="0 0 1200 320" preserveAspectRatio="none" aria-hidden="true">
    <path d="M0 202 C 260 120, 560 150, 760 180 C 960 200, 1110 120, 1200 20 L1200 108 C 1000 170, 820 210, 660 196 C 420 170, 200 160, 0 300 Z" fill="var(--band-blue)"/>
    <path d="M0 300 C 200 160, 420 170, 660 196 C 820 210, 1000 170, 1200 108 L1200 320 L0 320 Z" fill="var(--white)"/>
  </svg>

  <div class="side-stripe side-stripe--thin"></div>
  <div class="side-stripe side-stripe--wide"></div>

  <p class="intro">Discover tailored opportunities based on your career preferences</p>

  <ul class="specialties">
    <li>allied health</li>
    <li>nursing</li>
    <li>medical imaging</li>
  </ul>

  <h2 class="contact-title">Get in touch:</h2>
  <div class="contact-social">
    <div class="marker"></div>
    <span>@quellstaffing</span>
  </div>
  <p class="contact-web">www.quellstaffing.com.au</p>
</main>
</body>
</html>
```